CD Cover Design Project For New Electronic Album

Hi, I need cover artwork for my forth coming electronic music album. The requirement is for the single page front insert and also the tray liner (rear inlay). You can find the required specifications here http://www.brightpressing.example.co.uk/artwork_specs.php

The title of the album is Lumentide and the artists name is Owen Tasker.

The theme of the album is the world and water, so that needs to play a big part in the imagery. An example of the kind of thing I'm looking for can be found at

http://www.vistaplates.example.com/media/482730/view (this image is copyrighted, so please don't use for your own work).

I have no preference for the rear inlay, so please feel free to come up with something, so long as it is in keeping with the design for the front. There needs to be room for the song titles though, but not sure how many yet!

Good luck!
Updates

If you would like to hear a small section of the type of music to be on the album, you can listen at my tunevault account.

https://tunevault.example.com/quiet-lattice/sets/lumentide

This also contains a mock up of an album cover that was originally thought of, however permission could not be gained for the use of the image.

Industry/Entity Type

Electronic

```html
<!DOCTYPE html>
<html lang="en">
<head>
<meta charset="utf-8">
<title>Owen Tasker – Lumentide – Front</title>
<link rel="stylesheet" href="https://fonts.googleapis.com/css2?family=Montserrat:wght@800&family=Open+Sans:wght@300;400&display=swap">
<style>
  :root {
    --page: #ffffff;
    --cover-light: #f4f4f4;
    --cover-mid: #e9e9e9;
    --ink: #0b0b0b;
    --title: #ffffff;
    --globe-deep: #1b2021;
    --globe-sea: #2f6a70;
    --shadow: #8a8a8a;
  }
  html, body {
    margin: 0;
    width: 1200px;
    height: 1000px;
    overflow: hidden;
    background: var(--page);
  }
  .canvas {
    position: relative;
    width: 1200px;
    height: 1000px;
  }
  .cover {
    position: absolute;
    left: 258px;
    top: 158px;
    width: 684px;
    height: 685px;
    background: radial-gradient(ellipse at 50% 40%, var(--cover-light) 0%, var(--cover-mid) 100%);
    overflow: hidden;
  }
  .artist-name {
    position: absolute;
    top: 66px;
    left: 0;
    width: 100%;
    margin: 0;
    text-align: center;
    font-family: "Montserrat", sans-serif;
    font-weight: 800;
    font-size: 21px;
    letter-spacing: 3.6px;
    color: var(--ink);
    text-transform: uppercase;
  }
  .globe-artwork {
    position: absolute;
    left: 0;
    top: 0;
    width: 684px;
    height: 685px;
  }
  .album-title {
    position: absolute;
    top: 560px;
    left: 6px;
    width: 100%;
    margin: 0;
    text-align: center;
    font-family: "Open Sans", sans-serif;
    font-weight: 300;
    font-size: 33px;
    letter-spacing: 10px;
    color: var(--title);
    text-transform: uppercase;
  }
  .side-label {
    position: absolute;
    left: 258px;
    top: 868px;
    margin: 0;
    font-family: "Open Sans", sans-serif;
    font-weight: 400;
    font-size: 20px;
    color: var(--ink);
  }
</style>
</head>
<body>
<main class="canvas">
  <section class="cover">
    <svg class="globe-artwork" viewBox="0 0 684 685" role="img" aria-label="Illustration of a dark glass globe showing the continents in teal, with water droplets clinging to its edge and a soft grey shadow falling beneath it">
      <defs>
        <radialGradient id="shadow-fall" cx="50%" cy="50%" r="50%">
          <stop offset="0%" stop-color="var(--shadow)" stop-opacity="0.9"/>
          <stop offset="60%" stop-color="var(--shadow)" stop-opacity="0.45"/>
          <stop offset="100%" stop-color="var(--shadow)" stop-opacity="0"/>
        </radialGradient>
        <radialGradient id="globe-fill" cx="30%" cy="30%" r="75%">
          <stop offset="0%" stop-color="var(--globe-sea)"/>
          <stop offset="55%" stop-color="var(--globe-deep)"/>
          <stop offset="100%" stop-color="var(--globe-deep)"/>
        </radialGradient>
      </defs>
      <ellipse cx="342" cy="550" rx="230" ry="150" fill="url(#shadow-fall)"/>
      <circle cx="349" cy="340" r="155" fill="#ffffff" opacity="0.7"/>
      <circle cx="349" cy="340" r="151" fill="url(#globe-fill)" stroke="#9a9a9a" stroke-width="3"/>
    </svg>
    <h1 class="artist-name">Owen Tasker</h1>
    <h2 class="album-title">Lumentide</h2>
  </section>
  <p class="side-label">Front</p>
</main>
</body>
</html>
```